IT Services, Internet & Telephone Brochure

We need a new brochure that captures our core services. We have attached a pdf made in powerpoint providing the majority of content we would like. We have also included our telephone brochure as a example of colors and design that we liked. Lastly, we would like the designer to take liberty in developing a clean, professional but eye catching design.

```html
<!DOCTYPE html>
<html lang="en">
<head>
<meta charset="utf-8">
<title>Nexolink Services Brochure</title>
<link href="https://fonts.googleapis.com/css2?family=Roboto+Condensed:wght@400;700&family=Open+Sans:wght@600;700&family=Lato:wght@400&display=swap" rel="stylesheet">
<style>
  :root{
    --backdrop:#cfcfcf;
    --paper:#ffffff;
    --ink:#1c1c1c;
    --blue-deep:#1832f0;
    --blue-mid:#1a7cf5;
    --cyan:#1de6ff;
    --lime:#8be04a;
    --brand:#1a3cd8;
    --footer-text:#d2d8ff;
  }
  *{margin:0;padding:0;box-sizing:border-box}
  html,body{width:1200px;height:845px;overflow:hidden;background:var(--backdrop)}
  .canvas{position:relative;width:1200px;height:845px}
  .page{position:absolute;top:125px;width:435px;height:615px;background:var(--paper);overflow:hidden;
        font-family:"Roboto Condensed",sans-serif;color:#fff}
  .page--phone{left:148px}
  .page--services{left:623px}
  .page svg.shapes{position:absolute;inset:0;width:435px;height:615px}
  .t{position:absolute;white-space:nowrap;line-height:1}
  .c{transform:translateX(-50%)}
  .photo{position:absolute}
  .photo--deskphone{left:113px;top:5px;width:322px;height:250px;
        background:radial-gradient(ellipse at 60% 55%,#3a3d40 0%,#22252a 45%,#ffffff 72%)}
  .photo--tower{left:0;top:0;width:435px;height:310px;
        background:linear-gradient(180deg,#1f4fe0 0%,#2a6af0 45%,#6f94c8 70%,#3f8a2c 100%)}
  .heading{font-weight:700;letter-spacing:-.3px}
  .bold{font-weight:700}
  .benefits-title{font-family:"Lato",sans-serif;font-size:29px;left:4px;top:440px}
  .benefit{left:6px;font-size:10px}
  .option{font-size:8.6px}
  .price{font-size:8.2px}
  .feature{font-size:9.2px}
  .more-info{left:213px;top:592px;font-size:8.8px;color:var(--ink)}
  .services-bold{font-family:"Open Sans",sans-serif;font-weight:700}
  .svc{font-size:8.3px;line-height:11px}
  .brand-name{left:357px;top:352px;font-size:40px;font-weight:700;color:var(--brand)}
  .contact{top:591px;font-size:9px;color:var(--footer-text);display:flex;align-items:center;gap:4px}
  .contact svg{width:10px;height:10px}
  .sep{top:591px;font-size:9px;color:var(--footer-text)}
</style>
</head>
<body>
<div class="canvas">

  <!-- Telephone services page -->
  <section class="page page--phone">
    <div class="photo photo--deskphone" role="img" aria-label="Photo of a black office desk phone with display and keypad"></div>
    <svg class="shapes" viewBox="0 0 435 615" aria-hidden="true">
      <defs>
        <linearGradient id="blueSweepL" x1="0" y1="1" x2="1" y2="0">
          <stop offset="0" stop-color="var(--blue-deep)"/>
          <stop offset=".55" stop-color="var(--blue-mid)"/>
          <stop offset="1" stop-color="var(--cyan)"/>
        </linearGradient>
      </defs>
      <polygon points="200,268 435,268 435,570 230,570 60,340" fill="url(#blueSweepL)"/>
      <path d="M0,320 L52,382 Q57,388 64,384 L78,370 L222,552 Q230,565 222,578 L184,615 L0,615 Z" fill="var(--ink)"/>
      <path d="M78,370 L222,552 Q230,565 222,578 L184,615" fill="none" stroke="var(--lime)" stroke-width="1.2"/>
      <path d="M0,0 H17 L200,240 Q207,250 198,258 L62,370 Q55,376 48,368 L0,312 Z" fill="var(--ink)" stroke="#fff" stroke-width="3"/>
    </svg>

    <div class="t heading" style="left:5px;top:240px;font-size:15px">PHONE SERVICES - $19.95/MO</div>

    <div class="t heading c" style="left:302px;top:272px;font-size:18px">TELEPHONE OPTIONS:</div>
    <div class="t option c" style="left:298px;top:293px">- CORVANE C23 WITH THREE-WAY AUDIO CALLING,</div>
    <div class="t option c" style="left:298px;top:311px">2.8” BLACK &amp; WHITE LCD DISPLAY,</div>
    <div class="t option c" style="left:298px;top:329px">3 PROGRAMMABLE KEYS, WIRED HEADSET SUPPORT, ETC.</div>
    <div class="t option c" style="left:289px;top:354px">- CORVANE C29 WITH THREE-WAY AUDIO CALLING, 4.3” COLOR LCD DISPLAY,</div>
    <div class="t option c" style="left:289px;top:371px">10 PROGRAMMABLE KEYS, WIRELESS HEADSET SUPPORT, ETC.</div>

    <div class="t heading c" style="left:291px;top:391px;font-size:17px">TELEPHONE PRICING OPTIONS:</div>
    <div class="t price c" style="left:288px;top:410px">- CORVANE C23 PURCHASE FOR $75 EACH OR MONTHLY RENTAL OF $2.00/MO</div>
    <div class="t price c" style="left:290px;top:423px">- CORVANE C29 PURCHASE FOR $135 EACH OR MONTHLY RENTAL OF $3.50/MO</div>

    <div class="t heading c" style="left:308px;top:446px;font-size:14.5px">BUSINESS TELEPHONE FEATURES:</div>
    <div class="t feature c" style="left:308px;top:468px">CALLER-ID, CALL FORWARDING, CALL TRANSFER,</div>
    <div class="t feature c" style="left:308px;top:486px">VIRTUAL ASSISTANCE/AUTO ATTENDANT,</div>
    <div class="t feature c" style="left:308px;top:504px">SIMULTANEOUS RING,</div>
    <div class="t feature c" style="left:308px;top:522px">MOBILE APP, 1-LINE PER PHONE INCLUDED,</div>
    <div class="t feature c" style="left:308px;top:537px">1 TELEPHONE NUMBER PER PHONE INCLUDED</div>
    <div class="t feature c" style="left:308px;top:554px">AND MUCH MORE.</div>

    <div class="t benefits-title">BENEFITS</div>
    <div class="t benefit" style="top:486px">NO EXPENSIVE ONSITE</div>
    <div class="t benefit" style="top:505px">EASILY SCALE UP OR DOWN AS NEEDED</div>
    <div class="t benefit" style="top:524px">FREE TELEPHONE/EMAIL SUPPORT</div>
    <div class="t benefit" style="top:544px">LOWER MONTHLY COST</div>
    <div class="t benefit" style="top:563px">CUSTOMIZABLE TO YOUR BUSINESS</div>
    <div class="t benefit" style="top:582px">EASY SELF-ADMINISTRATION</div>

    <div class="t more-info">FOR MORE INFORMATION HEAD TO WWW.NEXOLINKIT.COM</div>
  </section>

  <!-- Internet and IT services page -->
  <section class="page page--services">
    <div class="photo photo--tower" role="img" aria-label="Photo of a tall office tower against blue sky with green trees"></div>
    <svg class="shapes" viewBox="0 0 435 615" aria-hidden="true">
      <defs>
        <linearGradient id="blueSweepR" x1="0" y1="1" x2="1" y2="0">
          <stop offset="0" stop-color="var(--blue-deep)"/>
          <stop offset=".55" stop-color="var(--blue-mid)"/>
          <stop offset="1" stop-color="var(--cyan)"/>
        </linearGradient>
      </defs>
      <path d="M0,261 H170 Q178,261 183,268 L213,305 H435 V572 H0 Z" fill="url(#blueSweepR)"/>
      <path d="M0,261 H170 Q178,261 183,268 L213,305 H435" fill="none" stroke="#fff" stroke-width="3"/>
      <path d="M232,313 H437 V441 H322 Q312,441 305,432 L226,326 Q222,313 232,313 Z" fill="var(--ink)" stroke="#fff" stroke-width="3"/>
      <path d="M25,578 H410 Q425,578 435,595 V615 H53 Z" fill="var(--ink)"/>
    </svg>

    <div class="t services-bold" style="left:8px;top:272px;font-size:13px">HIGH SPEED FIBER INTERNET</div>
    <div class="t" style="left:35px;top:299px;font-size:11px">BANDWIDTH OPTIONS:</div>
    <div class="t" style="left:11px;top:312px;font-size:11px">100MBPS STARTING AT $135/MO</div>
    <div class="t" style="left:11px;top:334px;font-size:11px">150MBPS STARTING AT $185/MO</div>
    <div class="t" style="left:11px;top:355px;font-size:11px">*PRICE VARIES DEPENDING ON LOCATION</div>

    <div class="t bold c" style="left:140px;top:377px;font-size:10px">FEATURES/BENEFITS:</div>
    <div class="t bold c" style="left:140px;top:391px;font-size:10px">DEDICATED SYMMETRICAL UPLINK &amp; DOWNLINK SPEEDS,</div>
    <div class="t bold c" style="left:140px;top:404px;font-size:10px">NO SLOW DOWN DURING PEAK TIMES,</div>
    <div class="t bold c" style="left:140px;top:417px;font-size:10px">99.99% UPTIME GUARANTEE,</div>
    <div class="t bold c" style="left:140px;top:430px;font-size:10px">STATIC IP ADDRESS, LOCAL SUPPORT.</div>

    <div class="t bold" style="left:261px;top:331px;font-size:8.4px;letter-spacing:-.3px">INTERNET-TELEPHONE-SECURITY-NETWORKING</div>
    <div class="t brand-name c">Nexolink</div>

    <div class="t services-bold c" style="left:206px;top:466px;font-size:16px">IT SERVICES</div>
    <div class="t services-bold svc" style="left:4px;top:493px">PC PROTECTION<br>SERVER PROTECTION<br>BACKUPS &amp; DISASTER RECOVERY<br>EMAIL/SPAM PROTECTION</div>
    <div class="t services-bold svc" style="left:149px;top:493px;line-height:12px">PC &amp; NETWORK HARDWARE SALES<br>SOFTWARE SALES<br>CONSULTING<br>CLOUD SERVICES</div>
    <div class="t services-bold svc" style="left:308px;top:494px;line-height:12px">RANSOMWARE PROTECTION<br>OFFICE SUITE<br>TROUBLESHOOTING/REPAIR<br>WIFI</div>

    <div class="t services-bold" style="left:26px;top:560px;font-size:9.6px;letter-spacing:-.2px">*STANDARD HOURLY RATE $75/HR OR CUSTOMIZED MONTHLY RATE FOR ALL SERVICES</div>

    <div class="t contact" style="left:76px">
      <svg viewBox="0 0 10 10" aria-hidden="true"><path d="M2,0.5 L3.6,2.6 L2.7,3.6 Q4,6.2 6.4,7.3 L7.4,6.4 L9.5,8 Q8.6,9.6 7,9.5 Q1,7.8 0.5,2.6 Q0.6,1 2,0.5 Z" fill="currentColor"/></svg>
      <span>555.010.2468</span>
    </div>
    <div class="t sep" style="left:161px">|</div>
    <div class="t contact" style="left:175px">
      <svg viewBox="0 0 10 10" aria-hidden="true"><rect x="0.5" y="2" width="9" height="6.5" fill="none" stroke="currentColor"/><path d="M0.5,2 L5,6 L9.5,2" fill="none" stroke="currentColor"/></svg>
      <span>sales@nexolinkit.com</span>
    </div>
    <div class="t sep" style="left:280px">|</div>
    <div class="t contact" style="left:294px">
      <svg viewBox="0 0 10 10" aria-hidden="true"><circle cx="5" cy="5" r="4.3" fill="none" stroke="currentColor"/><ellipse cx="5" cy="5" rx="1.8" ry="4.3" fill="none" stroke="currentColor"/><path d="M0.7,5 H9.3" stroke="currentColor"/></svg>
      <span>www.nexolinkit.com</span>
    </div>
  </section>

</div>
</body>
</html>
```